The title of the book is Beyond the Tidewater and the subtitle of the book is Walking Faith Through Rivers

I need a book cover that has a picture of a valley that is between two mountains. The picture needs to show mountains and a valley, not canyons and a valley. The focus should be on the valley. The attached covers are covers that I like with similar book titles. I would like for my name to be in all caps...DR. MARCUS J. HOLLOWAY

Target Market(s)

Religious: Christian: Spiritual: Ages 21 and up

Industry/Entity Type

Religious

Requirements
Must have
• I need to see mountains and a valley, not canyons and valleys. The designer must know the difference between a canyon and a mountain. Looking for a contemporary design.

```html
<!DOCTYPE html>
<html lang="en">
<head>
<meta charset="UTF-8">
<title>Beyond the Tidewater — Book Cover</title>
<link rel="stylesheet" href="https://fonts.googleapis.com/css2?family=Pinyon+Script&family=Barlow+Condensed:wght@700&family=Barlow+Semi+Condensed:wght@500&family=EB+Garamond:wght@500&display=swap">
<style>
  :root {
    --page-bg: #eeeeea;
    --sky-deep: #0c2740;
    --sky-mid: #17364d;
    --snow: #e6e2da;
    --slope-gold: #c9a064;
    --forest: #7d5a2a;
    --parchment-light: #efe2ab;
    --parchment: #e2cd88;
    --parchment-edge: #c9ad62;
    --title-navy: #123a52;
    --script-ink: #2a2118;
    --author-ink: #2f2b1c;
    --rule: #3b5566;
  }
  * { margin: 0; padding: 0; box-sizing: border-box; }
  html, body {
    width: 1200px;
    height: 1000px;
    overflow: hidden;
    background: var(--page-bg);
  }
  .book-cover {
    position: absolute;
    left: 300px;
    top: 50px;
    width: 600px;
    height: 900px;
    overflow: hidden;
    background:
      radial-gradient(ellipse at 50% 70%, var(--parchment-light) 0%, var(--parchment) 55%, var(--parchment-edge) 100%);
  }
  .cover-landscape {
    position: absolute;
    left: 0;
    top: 0;
    width: 600px;
    height: 560px;
    background: linear-gradient(180deg,
      var(--sky-deep) 0%,
      var(--sky-mid) 28%,
      var(--snow) 44%,
      var(--slope-gold) 58%,
      var(--forest) 74%,
      rgba(226, 205, 136, 0.6) 90%,
      rgba(226, 205, 136, 0) 100%);
  }
  .cover-title {
    position: absolute;
    left: 0;
    top: 480px;
    width: 600px;
    text-align: center;
  }
  .title-script {
    display: block;
    font-family: "Pinyon Script", cursive;
    font-size: 92px;
    line-height: 1;
    color: var(--script-ink);
    margin-left: 40px;
  }
  .title-main {
    display: block;
    font-family: "Barlow Condensed", sans-serif;
    font-weight: 700;
    font-size: 128px;
    line-height: 0.9;
    letter-spacing: 1px;
    color: var(--title-navy);
    margin-top: 8px;
  }
  .cover-subtitle {
    position: absolute;
    left: 0;
    top: 730px;
    width: 600px;
    display: flex;
    align-items: center;
    justify-content: center;
    gap: 14px;
    font-family: "EB Garamond", serif;
    font-weight: 500;
    font-size: 18px;
    letter-spacing: 0.5px;
    text-transform: uppercase;
    color: var(--title-navy);
  }
  .subtitle-rule {
    width: 60px;
    height: 1.5px;
    background: var(--rule);
  }
  .cover-author {
    position: absolute;
    left: 0;
    top: 788px;
    width: 600px;
    text-align: center;
    font-family: "Barlow Semi Condensed", sans-serif;
    font-weight: 500;
    font-size: 46px;
    letter-spacing: 0.5px;
    color: var(--author-ink);
  }
</style>
</head>
<body>
  <main class="book-cover">
    <div class="cover-landscape" role="img" aria-label="Photograph of a valley between two snow-capped mountains under a night sky with a full moon, autumn forest at the foot of the slopes"></div>
    <h1 class="cover-title">
      <span class="title-script">Beyond the</span>
      <span class="title-main">TIDEWATER</span>
    </h1>
    <p class="cover-subtitle">
      <span class="subtitle-rule"></span>
      <span class="subtitle-text">Walking Faith Through Rivers</span>
      <span class="subtitle-rule"></span>
    </p>
    <p class="cover-author">DR. MARCUS J. HOLLOWAY</p>
  </main>
</body>
</html>
```